International e-commerce business needs packaging design

We need a design that can be printed onto clear/see through Polypropylene bags to advertise our products and brand (We sell Electronic accessories such as cables and adapters but are expanding into other areas as well).
The bags we will be using will be of varying sizes ranging from roughly 15cm x 15cm up to 40cm x 40cm
We have attached a file (example 1 file) that show what we consider a good example of the sort of design we are looking for.
We would also like to have a new company logo as well though this is not critical so if someone comes up with a good alternative to our current design (also attached) we are more likely to choose a designer who comes up with a logo as well.
We are open to a complete revamp of the logo but we do want to keep the colour theme of rich red & grey/silver and also its shape (roughly).
In terms of details required in the packaging design there are a couple of things we require which should be straight forward enough...
1) Logo to be positioned top left (similar to example 1 file)
2) We need a "BLANK" white box suitable for affixing barcodes (similar to example 1 file) located bottom right area.
3) We need a safety warning along the very bottom warning of suffocation. The wording should read...
WARNING - risk of suffocation. Keep away from young children.
4) The colour theme should be rich red (like our current logo) and silvers/greys
5) In example 1 design the top right has the repeating words "computer accessories". We require another blank white box for us to put our own product descriptions in.
6) somewhere on the bag it should say our company name "Lumen Trove" with the "Registered" trademark logo on the end.
Thanks in advance to anyone who puts forward a design.
*UPDATE* We'd like to see binary code used within any design and have the below binary code which represents "Lumen Trove". It would be nice to incorporate this possibly in the logo but if not then certainly on any packaging design...
01001100 01110101 01101101 01100101 01101110 00100000 01010100 01110010 01101111 01110110 01100101
E-Commerce
- Calibri or Verdana

```html
<!DOCTYPE html>
<html lang="en">
<head>
<meta charset="utf-8">
<title>Lumen Trove – Packaging Bag Variants</title>
<link rel="stylesheet" href="https://fonts.googleapis.com/css2?family=Carlito:ital,wght@0,400;0,700;1,400&display=swap">
<style>
  :root {
    --red-rich: #c8000a;
    --red-deep: #7a0006;
    --red-shine: #e23a3a;
    --ink: #0d0d0d;
    --charcoal: #2b2b2b;
    --silver: #d9d9d9;
    --silver-light: #f1f1f1;
    --white: #ffffff;
    --clear-film: #f6f6f6;
    --hole-edge: #d4d4d4;
  }
  * { box-sizing: border-box; margin: 0; padding: 0; }
  html, body { width: 866px; height: 1200px; overflow: hidden; background: var(--white); }
  body { position: relative; font-family: "Carlito", Calibri, Verdana, sans-serif; }

  .bag {
    position: absolute;
    width: 370px;
    height: 553px;
    background: var(--clear-film);
    border: 1px solid #ececec;
    border-radius: 10px 10px 0 0;
    overflow: hidden;
  }
  .bag--one   { left: 38px;  top: 22px; }
  .bag--two   { left: 455px; top: 22px; }
  .bag--three { left: 42px;  top: 599px; }
  .bag--four  { left: 458px; top: 599px; }

  .hang-hole {
    position: absolute; left: 152px; top: 28px; width: 66px; height: 14px;
    border: 1px solid var(--hole-edge); border-radius: 7px; background: var(--white);
  }

  .brand-band {
    position: absolute; left: 0; top: 91px; width: 100%; height: 112px;
    background: linear-gradient(180deg, var(--red-shine) 0%, var(--red-rich) 45%, var(--red-deep) 100%);
  }
  .brand-band__hex {
    position: absolute; right: 0; top: 0; width: 150px; height: 92px;
    background: radial-gradient(circle at 60% 40%, #f08080 0%, #b0000a 55%, rgba(122,0,6,0) 100%);
    opacity: .85;
  }
  .brand-name {
    position: absolute; left: 14px; top: 32px;
    display: flex; align-items: center; gap: 8px;
    font-weight: 700; font-size: 30px; color: var(--charcoal); letter-spacing: .3px;
  }
  .brand-name__dot {
    width: 22px; height: 22px; border-radius: 50%; background: var(--silver);
  }
  .brand-name sup { font-size: 14px; }
  .tagline {
    position: absolute; left: 0; bottom: 0; width: 100%; height: 20px;
    background: linear-gradient(90deg, #3a0003, #1a0002);
    color: var(--white); font-weight: 700; font-size: 15px; line-height: 20px;
    text-align: center; white-space: nowrap;
  }
  .band-binary {
    position: absolute; left: 0; top: 4px; width: 100%;
    color: var(--white); font-weight: 700; font-style: italic; font-size: 9.5px;
    line-height: 11px; text-align: center;
  }

  .binary-strip {
    position: absolute; left: 0; top: 206px; width: 100%; height: 9px;
    background: var(--ink); color: var(--white); font-weight: 700;
    font-size: 6.5px; line-height: 9px; text-align: center; white-space: nowrap; overflow: hidden;
  }

  .product-window {
    position: absolute; left: 0; top: 215px; width: 100%; height: 246px;
    background: radial-gradient(ellipse at 45% 45%, #5a5a5a 0%, #2a2a2a 35%, var(--clear-film) 70%);
  }
  .code-label {
    position: absolute; left: 205px; top: 343px; width: 155px; height: 100px;
    background: var(--silver-light);
  }

  .base-band {
    position: absolute; left: 0; top: 461px; width: 100%; height: 92px;
    background: var(--ink);
  }
  .base-band::before {
    content: ""; position: absolute; left: 0; top: 5px; width: 100%; height: 2px; background: var(--white);
  }
  .bag--four .base-band { top: 447px; height: 106px; }

  .label-box {
    position: absolute; left: 220px; top: 483px; width: 135px; height: 57px;
    background: var(--white); border-radius: 8px;
  }
  .warning {
    position: absolute; left: 12px; top: 540px;
    color: var(--white); font-style: italic; font-size: 7px; white-space: nowrap;
  }
  .warning--stacked { left: 122px; top: 521px; line-height: 9px; }

  .binary-block {
    position: absolute; left: 8px; top: 410px; width: 120px;
    color: var(--white); font-weight: 700; font-size: 12px; line-height: 12.5px;
    text-shadow: 0 0 2px #000;
  }
  .binary-row {
    position: absolute; left: 165px; top: 452px; width: 200px;
    color: var(--white); font-weight: 700; font-size: 9.5px; line-height: 11px;
  }
</style>
</head>
<body>

  <!-- Variant: binary strip under tagline -->
  <section class="bag bag--one">
    <div class="hang-hole"></div>
    <div class="brand-band">
      <div class="brand-band__hex" role="img" aria-label="Glossy red hexagon cluster decoration"></div>
      <div class="brand-name"><span class="brand-name__dot"></span>Lumen Trove<sup>®</sup></div>
      <div class="tagline">Cables - Adapters - Electronic Accessories - Consumables</div>
    </div>
    <div class="binary-strip">01001100 01110101 01101101 01100101 01101110 00100000 01010100 01110010 01101111 01110110 01100101 01001100 01110101 01101101 01100101 01101110 00100000 01010100 01110010 01101111</div>
    <div class="product-window" role="img" aria-label="Clear window showing a coiled black cable with gold connectors"></div>
    <div class="code-label"></div>
    <div class="base-band"></div>
    <div class="label-box"></div>
    <p class="warning">WARNING - risk of suffocation. Keep away from young children.</p>
  </section>

  <!-- Variant: binary inside the brand band -->
  <section class="bag bag--two">
    <div class="hang-hole"></div>
    <div class="brand-band">
      <div class="brand-band__hex" role="img" aria-label="Glossy red hexagon cluster decoration"></div>
      <p class="band-binary">01001100 01110101 01101101 01100101 01101110 00100000<br>01010100 01110010 01101111 01110110 01100101</p>
      <div class="brand-name"><span class="brand-name__dot"></span>Lumen Trove<sup>®</sup></div>
      <div class="tagline">Cables - Adapters - Electronic Accessories - Consumables</div>
    </div>
    <div class="product-window" role="img" aria-label="Clear window showing a coiled black cable with gold connectors"></div>
    <div class="code-label"></div>
    <div class="base-band"></div>
    <div class="label-box"></div>
    <p class="warning">WARNING - risk of suffocation. Keep away from young children.</p>
  </section>

  <!-- Variant: binary block bottom left -->
  <section class="bag bag--three">
    <div class="hang-hole"></div>
    <div class="brand-band">
      <div class="brand-band__hex" role="img" aria-label="Glossy red hexagon cluster decoration"></div>
      <div class="brand-name"><span class="brand-name__dot"></span>Lumen Trove<sup>®</sup></div>
      <div class="tagline">Cables - Adapters - Electronic Accessories - Consumables</div>
    </div>
    <div class="product-window" role="img" aria-label="Clear window showing a coiled black cable with gold connectors"></div>
    <div class="code-label"></div>
    <div class="base-band"></div>
    <p class="binary-block">01001100 01110101<br>01101101 01100101<br>01101110 00100000<br>01010100 01110010<br>01101111 01110110<br>01100101</p>
    <div class="label-box"></div>
    <p class="warning warning--stacked">WARNING - risk of suffocation.<br>Keep away from young children.</p>
  </section>

  <!-- Variant: binary rows in base band -->
  <section class="bag bag--four">
    <div class="hang-hole"></div>
    <div class="brand-band">
      <div class="brand-band__hex" role="img" aria-label="Glossy red hexagon cluster decoration"></div>
      <div class="brand-name"><span class="brand-name__dot"></span>Lumen Trove<sup>®</sup></div>
      <div class="tagline">Cables - Adapters - Electronic Accessories - Consumables</div>
    </div>
    <div class="product-window" role="img" aria-label="Clear window showing a coiled black cable with gold connectors"></div>
    <div class="code-label"></div>
    <div class="base-band"></div>
    <p class="binary-row">01001100 01110101 01101101 01100101<br>01101110 00100000 01010100 01110010<br>01101111 01110110 01100101</p>
    <div class="label-box"></div>
    <p class="warning">WARNING - risk of suffocation. Keep away from young children.</p>
  </section>

</body>
</html>
```